Solo Law Practice Website Design

I am starting a solo law practice that will specialize in criminal defense and family law.

I have a rudimentary understanding of Wordpress as used through the hostmerry web services. The winning design would be compatible with this system so that I can modify content on my own.

I have supplied the written content and the components that I am looking for at the domain name: dorianvaskelaw.example.

I would like to take that content and work it into a website that looks more professional and inviting. The two most important goals of the website are ease of navigation and rich content for search engine spiders (for example, integrating articles into pages rather than linking to a word document).

The winning design should be turnkey for me to upload immediately.
Updates

Reason: I will be traveling.

Target Market(s)

Individuals looking for legal services.

Industry/Entity Type

Defense

Requirements
Must have
• My picture should appear at least once in the site.

The design should allow a space for me to post blog or legal updates. Additionally, there should be functionality for me to add additional articles to the site.
Nice to have
• Appropriate pictures for a legal website to break-up text on pages.

Simple flash features that won't significantly slow loading times.

Widgets that drive traffic to a contact page or function.

```html
<!DOCTYPE html>
<html lang="en">
<head>
<meta charset="utf-8">
<title>Law Offices of Dorian Vaske PLLC</title>
<link href="https://fonts.googleapis.com/css2?family=Oswald:wght@400;500;600&family=Arimo:wght@400;700&family=Crimson+Text:ital@0;1&display=swap" rel="stylesheet">
<style>
:root{
  --bg-deep:#0b2a45;
  --bg-mid:#134a73;
  --blue:#1d8fd6;
  --blue-dark:#0f6fb0;
  --blue-light:#3aa9ea;
  --link:#1273b8;
  --maroon:#5a1414;
  --text:#3c3c3c;
  --line:#c9c9c9;
  --gold:#f6e6a6;
  --parch:#ead9b4;
  --white:#ffffff;
}
*{box-sizing:border-box;margin:0;padding:0}
html,body{width:842px;height:1200px;overflow:hidden}
body{font-family:Arimo,Arial,sans-serif;color:var(--text);
  background:radial-gradient(ellipse at 50% 20%,var(--bg-mid) 0%,var(--bg-deep) 75%);}
.canvas{position:relative;width:842px;height:1200px;overflow:hidden}
.abs{position:absolute}

/* header */
.brand{left:80px;top:18px;width:253px;height:129px;background:linear-gradient(#f1e3c2,var(--parch));
  border:3px solid var(--blue-light);border-top:none;border-radius:0 0 18px 18px;text-align:center}
.brand-mark{position:absolute;left:103px;top:14px;width:46px;height:46px;border-radius:50%;background:#3b3226}
.brand-name{position:absolute;top:86px;left:0;width:100%;font-family:"Crimson Text",serif;font-size:15.5px;color:#3b3226}
.brand-tag{position:absolute;top:106px;left:0;width:100%;font-family:"Crimson Text",serif;font-size:8.5px;color:#3b3226}

.search{left:562px;top:35px;width:219px;height:24px;border:2px solid #6c8aa6;border-radius:3px;background:linear-gradient(#dfe6ee,#b7c6d4);}
.search span{position:absolute;left:6px;top:4px;font-size:9.5px;color:#555}
.search b{position:absolute;right:0;top:0;width:28px;height:20px;background:var(--blue);color:var(--bg-deep);font-family:Oswald,sans-serif;font-size:12px;line-height:20px;text-align:center}
.contact-row{left:562px;font-size:13.5px;font-weight:700;color:var(--gold);display:flex;align-items:center;gap:10px}

/* frame + nav */
.frame{left:61px;top:160px;width:720px;height:1002px;background:rgba(10,40,66,.55);border:1px solid #1c5885}
.ribbon-wing{left:0;top:181px;width:842px;height:42px;background:linear-gradient(var(--blue-light),var(--blue-dark))}
.nav{left:38px;top:171px;width:766px;height:39px;background:linear-gradient(#2fa3e8,var(--blue-dark));border:3px solid #52bdf5;
  display:flex;align-items:center;padding-left:33px}
.nav a{font-family:Oswald,sans-serif;font-size:11.5px;color:var(--white);text-decoration:none;padding:3px 11px}
.nav a.active{background:var(--blue-dark);border:1px solid #0a4f82}

/* hero */
.hero{left:76px;top:226px;width:690px;height:178px;background:linear-gradient(100deg,#3a1c0c,#7b4220 30%,#b06a2e 50%,#5a2e16 70%,#2a1a12)}
.caption{left:76px;top:404px;width:690px;height:45px;background:linear-gradient(#f3f3f3,#d8d8d8)}
.caption .welcome{position:absolute;left:12px;top:14px;font-family:Oswald,sans-serif;font-style:italic;font-size:13px;color:var(--blue)}
.caption .call{position:absolute;left:282px;top:9px;width:340px;font-family:"Crimson Text",serif;font-style:italic;font-size:10.5px;line-height:14px;color:#333}
.caption .split{position:absolute;left:265px;top:0;width:2px;height:45px;background:#bdbdbd}
.dots{position:absolute;right:8px;top:16px;display:flex;gap:4px}
.dots i{width:12px;height:12px;border-radius:50%;background:#333}
.dots i:first-child{background:var(--blue)}

/* content */
.sheet{left:76px;top:464px;width:690px;height:683px;background:var(--white)}
.main{left:98px;width:479px;font-size:9.1px;line-height:14.3px;text-align:justify}
.main b.lead{color:var(--link);font-weight:400}
.title{left:98px;top:483px;display:flex;align-items:center;gap:6px;font-family:Oswald,sans-serif;font-style:italic;font-weight:500;font-size:19px;line-height:24px;color:var(--maroon)}
.sub{font-size:10.5px;font-weight:700;color:#333}
.portrait{left:99px;top:596px;width:143px;height:96px;border:1px solid var(--line);padding:4px;background:#fff}
.portrait div{width:100%;height:100%;background:linear-gradient(135deg,#c9a27a,#8a5a3a)}
.more{color:var(--link);font-weight:700;font-size:9.5px}

.form-title{left:98px;top:937px;display:flex;align-items:center;gap:6px;font-family:Oswald,sans-serif;font-style:italic;font-size:18px;line-height:20px;color:var(--maroon)}
.form-sub{left:99px;top:960px;font-size:10px;line-height:12px;letter-spacing:2px;color:#888}
.label{font-size:9.5px;font-weight:700;color:var(--link);letter-spacing:.6px}
.field{border:1px solid var(--line);background:#fff}
.send{left:481px;top:1117px;width:87px;height:21px;background:var(--blue);color:#fff;font-family:Oswald,sans-serif;font-size:11px;line-height:21px;text-align:center}

/* sidebar */
.side{left:581px;width:185px;overflow:hidden}
.side-head{height:37px;background:var(--blue);display:flex;align-items:center;gap:8px;padding-left:13px;
  font-family:Oswald,sans-serif;font-style:italic;font-size:14px;color:#fff}
.side-body{background:#ececec}
.rules a{display:block;margin:0 10px 0 11px;height:24.4px;line-height:24px;border-bottom:1px solid var(--line);font-size:8.6px;letter-spacing:.3px;color:#555;text-decoration:none;white-space:nowrap}
.side-text{font-size:9px;color:#555;line-height:15px}
.map{left:592px;top:932px;width:163px;height:205px;border:1px solid #bbb;background:linear-gradient(135deg,#e9e4d6,#d7e3c8 50%,#e6e0cf)}

/* footer */
.footer{left:0;top:1175px;width:842px;text-align:center;font-size:9px;color:#6f8fac;line-height:14px}
.footer a{color:#6f8fac;text-decoration:none}
.footer em{font-style:normal;color:var(--blue)}
</style>
</head>
<body>
<div class="canvas">

  <div class="abs brand">
    <span class="brand-mark"></span>
    <div class="brand-name">Law Offices of Dorian Vaske PLLC</div>
    <div class="brand-tag">Specializing in Criminal Defense and Family Law</div>
  </div>

  <div class="abs search"><span>Search...</span><b>GO</b></div>
  <div class="abs contact-row" style="top:74px">
    <svg width="20" height="20" viewBox="0 0 20 20"><circle cx="10" cy="10" r="9" fill="none" stroke="#4aa6e6" stroke-width="1.5"/><path d="M7 5.5c-1 1 -1 3 1 6s4 3.5 5 2.5l-1.5-2-1.2.6c-1-.6-2-2-2.3-3l1-.8z" fill="#4aa6e6"/></svg>
    <span>(612)555-0148</span>
  </div>
  <div class="abs contact-row" style="top:100px">
    <svg width="20" height="16" viewBox="0 0 20 16"><rect x="1" y="1" width="18" height="14" fill="#4aa6e6"/><path d="M1 1l9 8 9-8" fill="none" stroke="#0b2a45" stroke-width="1.4"/></svg>
    <span>Dorian@dorianvaskelaw.example</span>
  </div>

  <div class="abs frame"></div>
  <div class="abs ribbon-wing"></div>
  <nav class="abs nav">
    <a class="active">Home</a><a>Contact Me</a><a>Criminal Law</a><a>Family Law</a><a>Will Drafting</a><a>Attorney Profile</a><a>Fees</a><a>Legal Updates</a><a>Online Resources</a><a>Articles</a>
  </nav>

  <div class="abs hero" role="img" aria-label="Photo of a wooden gavel in a law library beside a smiling attorney in a suit"></div>
  <div class="abs caption">
    <div class="welcome">WELCOME TO LAW OFFICES OF DORIAN VASKE PLLC</div>
    <div class="split"></div>
    <div class="call">To discuss how the Law Offices of Dorian Vaske can help you, call us at (612) 555-0148 to arrange for you free consultation.</div>
    <div class="dots"><i></i><i></i><i></i></div>
  </div>

  <div class="abs sheet"></div>

  <h1 class="abs title">
    <svg width="20" height="18" viewBox="0 0 20 18"><path d="M10 1L1 9h3v8h4v-5h4v5h4V9h3z" fill="#1d8fd6"/></svg>
    SPECIALIZING IN CRIMINAL DEFENSE AND FAMILY LAW
  </h1>
  <div class="abs main sub" style="top:514px">Delivering legal services in the greater Twin Cities area.</div>
  <p class="abs main" style="top:531px"><b class="lead">About Me.</b> My practice is focused on accomplishing your goals through results-oriented work at a discount price. For your convenience, I handle legal matters throughout the Twin Cities, including Hennepin, Ramsey, Anoka, and Washington counties. I understand that legal issues can appear complicated, and that is why I take a hands-on approach to guiding you through your legal needs.</p>

  <div class="abs portrait"><div role="img" aria-label="Portrait photo of the attorney"></div></div>
  <p class="abs main" style="top:595px;left:257px;width:320px"><b class="lead">Personal Attention.</b> I control the size of my practice so that I am able to devote 100% of my effort to each case. I have no "associates" so I handle every case personally.<br><b class="lead">General Practice.</b> I am available to provide your defense if you are accused of a felony or misdemeanor. Additionally, I can work with you on family matters such as divorce, child custody, wills, and nuptial agreements.<br><span class="more">Learn More »</span></p>

  <div class="abs main sub" style="top:702px">My areas of specialization are as follows:</div>
  <p class="abs main" style="top:718px"><b class="lead">Criminal Law.</b> Convictions carry serious consequences and can often have a negative financial impact as well as putting your freedom in jeopardy. I know how to work on your behalf because I used to work at the Ramsey County Attorney's Office and appeared on the prosecution's behalf for more than 600 cases. I will prepare your defense, negotiate plea bargains if desired, or take the case to trial.</p>
  <p class="abs main" style="top:783px"><b class="lead">Experience Matters.</b> Every case is different. You can take comfort knowing that I have appeared in court on a wide variety of cases including assault, drug possession and distribution, DWI, disorderly conduct, theft, burglary, domestic assault, check forgery, violations or orders for protection, firearms violations and DWI test refusals. I am also prepared to handle your probation violation or expungement.</p>
  <p class="abs main" style="top:850px"><b class="lead">Family Law.</b> I am prepared to handle your family law concerns. I can guide you through the process of child custody matters, divorce, wills and nuptial agreements to ensure that you receive a fair and equitable result on these sensitive matters.</p>
  <p class="abs main" style="top:902px"><b class="lead">Contact me.</b> To discuss how the Law Offices of Dorian Vaske can help you, call us at (612) 555-0148 to arrange for you free consultation.</p>

  <h2 class="abs form-title">
    <svg width="20" height="15" viewBox="0 0 20 15"><rect x="1" y="1" width="18" height="13" fill="#1d8fd6"/><path d="M1 1l9 7 9-7" fill="none" stroke="#fff" stroke-width="1.3"/></svg>
    CONTACT FORM
  </h2>
  <div class="abs form-sub">WE WILL ASNWER WITHIN 24 HOURS</div>
  <div class="abs label" style="left:102px;top:987px">Your Name:</div>
  <div class="abs field" style="left:100px;top:1001px;width:218px;height:23px"></div>
  <div class="abs label" style="left:102px;top:1029px">Phone Number:</div>
  <div class="abs field" style="left:100px;top:1044px;width:218px;height:22px"></div>
  <div class="abs label" style="left:102px;top:1072px">Email Address:</div>
  <div class="abs field" style="left:100px;top:1086px;width:218px;height:22px"></div>
  <div class="abs label" style="left:332px;top:987px">Message:</div>
  <div class="abs field" style="left:331px;top:1001px;width:236px;height:107px"></div>
  <div class="abs send">SEND MESSAGE</div>

  <aside class="abs side" style="top:464px;height:205px">
    <div class="side-head"><svg width="24" height="16" viewBox="0 0 24 16"><path d="M3 12l8-10h11l-8 10z" fill="#0c3d64"/><path d="M3 12h11v3H3z" fill="#0c3d64"/></svg>RULES AND LAWS</div>
    <div class="side-body rules" style="height:168px;padding-top:8px">
      <a>Minnesota Rules of Evidence</a><a>Rules of the Court</a><a>Minnesota Rules of Criminal Procedure</a><a>Minnesota Rules of Civil Procedure</a><a>Minnesota Legislature</a><a>Criminal Statutes</a>
    </div>
  </aside>

  <aside class="abs side" style="top:669px;height:106px">
    <div class="side-head"><svg width="22" height="15" viewBox="0 0 22 15"><rect x="1" y="1" width="20" height="13" fill="#0c3d64"/><path d="M1 1l10 7 10-7" fill="none" stroke="#1d8fd6" stroke-width="1.3"/></svg>NEWSLETTER</div>
    <div class="side-body" style="height:69px;position:relative">
      <div class="side-text" style="position:absolute;left:11px;top:11px">Your Name:</div>
      <div class="field" style="position:absolute;left:11px;top:25px;width:137px;height:22px"></div>
      <div style="position:absolute;left:148px;top:25px;width:25px;height:22px;background:var(--blue);color:#fff;font-family:Oswald,sans-serif;font-size:12px;line-height:22px;text-align:center">GO</div>
    </div>
  </aside>

  <aside class="abs side" style="top:775px;height:109px">
    <div class="side-head"><svg width="22" height="15" viewBox="0 0 22 15"><rect x="1" y="1" width="20" height="13" fill="#0c3d64"/><path d="M1 1l10 7 10-7" fill="none" stroke="#1d8fd6" stroke-width="1.3"/></svg>CONTACT US</div>
    <div class="side-body side-text" style="height:72px;padding:10px 11px">
      Law Offices of Dorian Vaske PLLC<br>Phone: (612)555-0148<br>Email:Dorian@dorianvaskelaw.example
    </div>
  </aside>

  <aside class="abs side" style="top:884px;height:263px">
    <div class="side-head"><svg width="26" height="20" viewBox="0 0 26 20"><path d="M2 6l7-3 8 3 7-3v12l-7 3-8-3-7 3z" fill="#0c3d64"/></svg>MAP</div>
    <div class="side-body" style="height:226px"></div>
  </aside>
  <div class="abs map" role="img" aria-label="Street map showing the office location"></div>

  <footer class="abs footer">
    <div><a>Home</a> | <a>Criminal Law</a> | <a>Family Law</a> | <a>Will Drafting</a> | <a>Attorney Profile</a> | <a>Fees</a> | <a>Legal Updates</a> | <a>Online Resources</a> | <a>Articles</a> | <a>Contact Me</a></div>
    <div>©Copyright 2012. All Rights Reserved. Site by <em>Law Offices of Dorian Vaske PLLC</em></div>
  </footer>

</div>
</body>
</html>
```